Business Card Design For A Cajun Seafood Restaurant

We are opening a cajun seafood restaurant in a week. We mainly serve cajun seafood which is orginally from Louisiana. We want design on both sides of a business card. I have menu on the website. You can go to www.bayourelish.com to check out our menu.

Restaurant name: Bayou Relish
Phone: +1 (555) 555-4172
Address: 48627 Dellmont Row, #5, Fernvale, Ca95999
Email: bayourelish@mailbox.example
Website: www.bayourelish.com

Maybe add social media icons (facebook, instagram) if looks nice on the business card.
facebook.com/bayourelish
instagram.com/bayourelish or @bayourelish

Attached is the logo and other business card samples that I like.

```html
<!DOCTYPE html>
<html lang="en">
<head>
<meta charset="utf-8">
<title>Bayou Relish – Business Card</title>
<link rel="stylesheet" href="https://fonts.googleapis.com/css2?family=Lato:wght@400;700;900&display=swap">
<style>
  :root {
    --stage: #bdbdbd;
    --ink: #0b0b0b;
    --paper: #ffffff;
    --accent: #f26a1b;
    --text: #1e1e1e;
    --muted: #3a3a3a;
    --social-alt: #4f6fb5;
  }
  * { box-sizing: border-box; margin: 0; padding: 0; }
  html, body { width: 1200px; height: 837px; overflow: hidden; }
  body {
    background: var(--stage);
    font-family: "Lato", Arial, sans-serif;
    position: relative;
  }
  .card {
    position: absolute;
    top: 264px;
    width: 540px;
    height: 309px;
    border-radius: 2px;
    box-shadow: 0 10px 24px rgba(0,0,0,.22);
    overflow: hidden;
  }

  /* Dark side */
  .card--front { left: 45px; background: var(--ink); }
  .brand {
    position: absolute; left: 50%; top: 50%;
    transform: translate(-50%, -50%);
    display: flex; flex-direction: column; align-items: center; gap: 10px;
  }
  .brand__row { display: flex; align-items: center; gap: 14px; }
  .brand__dot { width: 22px; height: 22px; border-radius: 50%; background: var(--accent); }
  .brand__name {
    color: var(--accent);
    font-weight: 900;
    font-size: 40px;
    letter-spacing: 1px;
    white-space: nowrap;
  }
  .brand__tagline {
    color: var(--paper);
    font-weight: 700;
    font-size: 13px;
    letter-spacing: 3px;
    text-transform: uppercase;
  }

  /* White side */
  .card--back { left: 615px; background: var(--paper); }
  .back__logo {
    position: absolute; left: 20px; top: 50px;
    width: 200px; height: 140px;
    display: flex; align-items: center; justify-content: center; gap: 10px;
  }
  .back__logo-mark { width: 18px; height: 18px; border-radius: 50%; background: var(--accent); flex: none; }
  .back__logo-name { color: var(--accent); font-weight: 900; font-size: 24px; white-space: nowrap; }
  .back__divider {
    position: absolute; left: 232px; top: 32px;
    width: 1px; height: 168px; background: var(--muted);
  }
  .contact {
    position: absolute; left: 252px; top: 38px; right: 14px;
    color: var(--text);
  }
  .contact__name { color: var(--accent); font-weight: 900; font-size: 20px; line-height: 1.1; }
  .contact__role { font-size: 12.5px; margin-bottom: 14px; }
  .contact__address { font-size: 12.5px; line-height: 1.4; margin-bottom: 8px; }
  .contact__line {
    display: flex; align-items: center; gap: 7px;
    font-size: 12.5px; line-height: 1.3; margin-bottom: 5px;
    white-space: nowrap;
  }
  .icon {
    width: 16px; height: 16px; border-radius: 2px;
    background: var(--accent); flex: none;
    display: flex; align-items: center; justify-content: center;
  }
  .social { display: flex; align-items: center; gap: 6px; margin-top: 10px; font-size: 12.5px; }
  .social__square { width: 20px; height: 20px; border-radius: 2px; background: var(--accent); }
  .social__square--alt { background: var(--social-alt); }
  .social__handle { margin-left: 10px; }
  .back__rule {
    position: absolute; left: 0; right: 0; top: 232px;
    height: 2px; background: var(--accent);
  }
  .back__band {
    position: absolute; left: 0; right: 0; top: 240px; bottom: 0;
    background: var(--ink);
    display: flex; align-items: center; justify-content: center;
    color: var(--paper); font-size: 14px; letter-spacing: .5px;
  }
  .back__band .domain { color: var(--accent); }
</style>
</head>
<body>

  <section class="card card--front" aria-label="Business card, front">
    <div class="brand">
      <div class="brand__row">
        <span class="brand__dot"></span>
        <span class="brand__name">Bayou Relish</span>
      </div>
      <div class="brand__tagline">Gulf Kitchen &amp; Boil</div>
    </div>
  </section>

  <section class="card card--back" aria-label="Business card, back">
    <div class="back__logo">
      <span class="back__logo-mark"></span>
      <span class="back__logo-name">Bayou Relish</span>
    </div>
    <div class="back__divider"></div>

    <div class="contact">
      <p class="contact__name">Dana Whitfield</p>
      <p class="contact__role">Managing Director</p>
      <p class="contact__address">48627 Dellmont Row, #5<br>Fernvale, Ca95999</p>
      <p class="contact__line">
        <span class="icon">
          <svg width="10" height="10" viewBox="0 0 24 24"><path fill="#fff" d="M6.6 10.8a15 15 0 0 0 6.6 6.6l2.2-2.2c.3-.3.7-.4 1-.2 1.1.4 2.3.6 3.6.6.6 0 1 .4 1 1V20c0 .6-.4 1-1 1A17 17 0 0 1 3 4c0-.6.4-1 1-1h3.5c.6 0 1 .4 1 1 0 1.3.2 2.5.6 3.6.1.3 0 .7-.2 1z"/></svg>
        </span>
        +1 (555) 555-4172
      </p>
      <p class="contact__line">
        <span class="icon">
          <svg width="10" height="10" viewBox="0 0 24 24"><path fill="none" stroke="#fff" stroke-width="2.4" d="M3 6h18v12H3z M3 6l9 7 9-7"/></svg>
        </span>
        bayourelish@mailbox.example
      </p>
      <div class="social">
        <span class="social__square social__square--alt"></span>
        <span class="social__square"></span>
        <span class="social__handle">bayourelish</span>
      </div>
    </div>

    <div class="back__rule"></div>
    <div class="back__band">www.<span class="domain">bayourelish</span>.com</div>
  </section>

</body>
</html>
```